Guaranteed Job - Sleek Sexy Business Card UV Spot

Im looking for a sleek and sexy business card, that resembles elite or VIP status status.
our business is corinvale.example
you can view our products on there, but our main audience for handing out our cards will be for people in the hospitality industry, so it will need to impress high management and CEO of hotels and restaurants, bars, clubs etc...
the card features will have UV spot on both sides, 400gsm stock. standard size.
Artwork should be 86 x 54mm + 2mm bleed = 90 x 58mm
it should have a nice "unique" uv spot pattern that highlights the card, not a repeated pattern, theres no originality there, and it will be disregarded.
The written material will be:
Corin Vale Hospitality College (logo)
Tobin Marsh
Director
Phone: 1300 615 737
Mobile: 0455 817 296
Email: info@corinvale.example
website: www.corinvale.example
I'm looking for originality here, i don't want just a simple stock card, want something that has a wow factor for people.
You will find the logo attached. you may invert the white to black words to suit the background as you please.
thank you and good luck
As a side note, ive received a lot of proposals, im too busy to give feedback to each and every one, so if i havent provided feedback for your design within 24 hours, then consider it not acceptable, and you could resubmit another design.
So far i have not seen any design that stood out for me, they all seem pretty generic. there nothing thats unique, i would figure for the amount that im offering, that people would put some more effort and creativity into the design.
so far over 200 designs submitted, and nothing i have seen looks very original, everything looks like a different variation of the same stuff, i said it very clearly i wanted something unique, the only thing that has come close to it so far is this one
Reason: Ive received alot of design concepts and i have reviewed everyone, but i havent had time to give feedback to every single one, only the ones that have interested me, if i havent responded, its because i havent found it good enough.
so far only a few design have been on par with what ive been looking for, an attractive eye popping design.
heres a few of them,
http://files.pixelbazaar.example/design_img/51736/62418/62418_2840915_51736_image.jpg
http://files.pixelbazaar.example/design_img/51736/68254/68254_2841377_51736_image.jpg
theyre, both unique and original, and eye catching, the only thing theyre missing is the sexyness.
if you still think you have some creativity left in your minds, then throw it on here.
Reason: Sorry guys for the delay, I was in a serious accident and out of commission for the past few months, I'm just slowly recovering now, please bare with me as i try to attend to this project, it may take me awhile as I have other projects that are on standby, I'm not 100% at the moment, so im extending the deadline for 2 weeks right now. Thanks for your patience.
Hospitality

```html
<!DOCTYPE html>
<html lang="en">
<head>
<meta charset="utf-8">
<title>Corin Vale Hospitality College – Business Card</title>
<link rel="stylesheet" href="https://fonts.googleapis.com/css2?family=Questrial&family=Barlow+Semi+Condensed:wght@600&display=swap">
<style>
  :root {
    --page: #e8e5e1;
    --card-dark: #151515;
    --card-mid: #262626;
    --sky: #5aaee2;
    --ink-white: #ffffff;
    --ink-line: #8a8a8a;
    --text-font: "Questrial", sans-serif;
    --brand-font: "Barlow Semi Condensed", sans-serif;
  }
  * { margin: 0; padding: 0; box-sizing: border-box; }
  html, body {
    width: 1053px;
    height: 1200px;
    overflow: hidden;
    background: var(--page);
  }
  .sheet {
    position: relative;
    width: 1053px;
    height: 1200px;
  }
  .card {
    position: absolute;
    left: 181px;
    width: 690px;
    height: 434px;
    overflow: hidden;
    border: 1px solid var(--ink-line);
    background:
      linear-gradient(180deg, rgba(255,255,255,0.05) 0%, rgba(255,255,255,0) 40%, rgba(0,0,0,0.25) 100%),
      linear-gradient(90deg, var(--card-dark) 0%, var(--card-mid) 50%, var(--card-dark) 100%);
  }
  .card--front { top: 122px; }
  .card--back { top: 641px; }

  .v-band {
    position: absolute;
    inset: 0;
    width: 100%;
    height: 100%;
  }

  .holder {
    position: absolute;
    top: 26px;
    left: 0;
    width: 100%;
    text-align: center;
    font-family: var(--text-font);
  }
  .holder__name {
    font-size: 35px;
    color: var(--sky);
    font-weight: 400;
    letter-spacing: 0.5px;
    -webkit-text-stroke: 0.6px var(--sky);
  }
  .holder__role {
    margin-top: 4px;
    font-size: 25px;
    color: var(--ink-white);
  }

  .brand {
    position: absolute;
    display: flex;
    align-items: center;
    gap: 14px;
    font-family: var(--brand-font);
    font-weight: 600;
    color: var(--ink-white);
    text-transform: uppercase;
  }
  .brand__mark {
    flex: none;
    border-radius: 50%;
  }
  .brand__name {
    line-height: 0.95;
  }
  .brand--front {
    top: 128px;
    left: 50%;
    transform: translateX(-50%);
    font-size: 31px;
  }
  .brand--front .brand__mark {
    width: 62px;
    height: 62px;
    background: var(--ink-white);
  }
  .brand--back {
    top: 160px;
    left: 50%;
    transform: translateX(-50%);
    font-size: 52px;
    gap: 26px;
  }
  .brand--back .brand__mark {
    width: 120px;
    height: 120px;
    background: var(--sky);
  }

  .contacts {
    position: absolute;
    top: 275px;
    left: 0;
    width: 100%;
    list-style: none;
    font-family: var(--text-font);
    font-size: 21px;
    color: var(--ink-white);
  }
  .contacts__item {
    display: flex;
    justify-content: center;
    align-items: center;
    gap: 9px;
    height: 39px;
  }
  .contacts__icon {
    width: 15px;
    height: 15px;
    flex: none;
  }
</style>
</head>
<body>
<main class="sheet">

  <section class="card card--front" aria-label="Card front">
    <svg class="v-band" viewBox="0 0 524 330" preserveAspectRatio="none" aria-hidden="true">
      <path d="M0 0 H524 L359 330 H173 Z M139 0 L169 84 H364 L401 0 Z" fill="#5aaee2" fill-rule="evenodd"/>
    </svg>

    <header class="holder">
      <h1 class="holder__name">Tobin Marsh</h1>
      <p class="holder__role">Director</p>
    </header>

    <div class="brand brand--front">
      <span class="brand__mark" aria-hidden="true"></span>
      <span class="brand__name">Corin Vale<br>Hospitality College</span>
    </div>

    <ul class="contacts">
      <li class="contacts__item">
        <svg class="contacts__icon" viewBox="0 0 16 16" aria-hidden="true"><path d="M1 4h14v9H1z M1 4l7 5 7-5" fill="none" stroke="#fff" stroke-width="1.6"/></svg>
        <span>info@corinvale.example</span>
      </li>
      <li class="contacts__item">
        <svg class="contacts__icon" viewBox="0 0 16 16" aria-hidden="true"><g fill="none" stroke="#fff" stroke-width="1.3"><circle cx="8" cy="8" r="6.5"/><ellipse cx="8" cy="8" rx="3" ry="6.5"/><path d="M1.5 8h13"/></g></svg>
        <span>www.corinvale.example</span>
      </li>
      <li class="contacts__item">
        <svg class="contacts__icon" viewBox="0 0 16 16" aria-hidden="true"><path d="M4 1.5l3 3-1.8 1.8a9 9 0 0 0 4.5 4.5L11.5 9l3 3-2 2.5C7 14 2 9 1.5 3.5z" fill="#fff"/></svg>
        <span>1300 615 737</span>
      </li>
      <li class="contacts__item">
        <svg class="contacts__icon" viewBox="0 0 16 16" aria-hidden="true"><rect x="4" y="1" width="8" height="14" rx="1.5" fill="#fff"/><rect x="5.5" y="3" width="5" height="6" fill="#5aaee2"/></svg>
        <span>0455 817 296</span>
      </li>
    </ul>
  </section>

  <section class="card card--back" aria-label="Card back">
    <div class="brand brand--back">
      <span class="brand__mark" aria-hidden="true"></span>
      <span class="brand__name">Corin Vale<br>Hospitality College</span>
    </div>
  </section>

</main>
</body>
</html>
```